Life Coaching Business Card

Please check out my website at www.lorettavanmeer.example. Ideally I would like to use the same colors that I used on the site to match my business cards i.e: pink, green, teal, white
I want the final design to include a picture of me and also to be appealing and eye catching. For the picture I submitted, you can crop it smaller to just have my face (exclude my chest) showing.
Industry/Entity Type
Business
Contact Information for Business Card
Loretta Vanmeer
Transformational Life Coach
web: www.lorettavanmeer.example
email: loretta@lorettavanmeer.example
Phone: 555-318-4072
Look and feel
Each slider illustrates characteristics of the customer's brand and the style your logo design should communicate.

```html
<!DOCTYPE html>
<html lang="en">
<head>
<meta charset="utf-8">
<title>Loretta Vanmeer — Business Card</title>
<link rel="stylesheet" href="https://fonts.googleapis.com/css2?family=Abril+Fatface&family=Crimson+Text:wght@400;600;700&family=Open+Sans:wght@400;600&display=swap">
<style>
  :root {
    --page: #ffffff;
    --night: #141414;
    --dusk: #3a3a3a;
    --haze: #6f6f6f;
    --silver-light: #e9e9e9;
    --silver-dark: #9a9a9a;
    --ink: #1b1b1b;
    --lime: #8cc63f;
    --lime-deep: #6fa52b;
    --lime-soft: #a3d45a;
    --magenta: #b0299f;
    --magenta-glow: #e25be0;
    --strip: #c4c6c8;
    --strip-icon: #e4e6e7;
    --white: #ffffff;
  }
  * { box-sizing: border-box; margin: 0; padding: 0; }
  html, body {
    width: 940px; height: 1200px; overflow: hidden;
    background: var(--page);
  }
  .sheet { position: relative; width: 940px; height: 1200px; }

  .card {
    position: absolute; left: 113px; width: 729px; height: 420px;
    overflow: hidden;
  }
  .card--front { top: 141px; }
  .card--back { top: 635px; }

  .scene {
    position: absolute; inset: 0;
    background:
      radial-gradient(ellipse 60% 40% at 62% 45%, var(--haze) 0%, transparent 70%),
      linear-gradient(180deg, var(--night) 0%, var(--dusk) 45%, #4a4a4a 55%, var(--night) 100%);
  }

  /* Front */
  .portrait {
    position: absolute; left: 0; top: 0; width: 125px; height: 100%;
    background: linear-gradient(90deg, #2a2a2a 0%, #8a8a8a 45%, #5a5a5a 100%);
  }
  .band { position: absolute; left: 10px; right: 0; display: flex; align-items: center; justify-content: center; }
  .band--name {
    top: 103px; height: 76px;
    background: linear-gradient(180deg, var(--silver-light) 0%, #d2d2d2 60%, var(--silver-dark) 100%);
  }
  .band--title {
    top: 203px; height: 38px;
    background: linear-gradient(90deg, var(--lime-deep) 0%, var(--lime) 30%, var(--lime-soft) 70%, var(--lime-deep) 100%);
  }
  .band--web {
    top: 244px; height: 44px;
    background: linear-gradient(90deg, #6a1462 0%, var(--magenta) 20%, var(--magenta-glow) 60%, #5a0f55 100%);
  }
  .owner-name {
    font-family: "Abril Fatface", serif;
    font-size: 50px; color: var(--ink); letter-spacing: 1px;
    margin-left: 70px;
  }
  .owner-title {
    font-family: "Open Sans", sans-serif; font-weight: 400;
    font-size: 25px; color: var(--white); letter-spacing: 1.5px;
    margin-left: 70px;
  }
  .owner-web {
    font-family: "Crimson Text", serif;
    font-size: 26px; color: var(--white);
    margin-left: 70px;
  }

  /* Back */
  .icon-strip {
    position: absolute; left: 126px; top: 0; width: 96px; height: 100%;
    background: var(--strip); opacity: 0.85;
  }
  .divider {
    position: absolute; left: 222px; top: 0; width: 4px; height: 100%;
    background: #1e1e1e;
  }
  .contact-panel {
    position: absolute; left: 226px; top: 0; width: 376px; height: 100%;
    display: flex; flex-direction: column;
  }
  .contact-row {
    flex: 1; display: flex; align-items: center; padding-left: 24px;
    background: var(--lime);
    border-bottom: 1px solid rgba(255,255,255,0.18);
    color: var(--white);
  }
  .contact-row:nth-child(even) { background: #86c03b; }
  .contact-row:last-child { border-bottom: none; }
  .arrow { width: 9px; height: 12px; margin-right: 12px; flex: none; }
  .contact-name {
    font-family: "Crimson Text", serif; font-weight: 700;
    font-variant: small-caps; font-size: 25px; letter-spacing: 1px;
  }
  .contact-text {
    font-family: "Open Sans", sans-serif; font-size: 18px;
  }
  .strip-icon {
    position: absolute; left: 150px; width: 48px; height: 48px;
  }
</style>
</head>
<body>
<main class="sheet">

  <section class="card card--front">
    <div class="scene" role="img" aria-label="Blurred black and white photo of an open road stretching to the horizon"></div>
    <div class="portrait" role="img" aria-label="Black and white portrait photo of the coach"></div>
    <div class="band band--name"><h1 class="owner-name">Loretta Vanmeer</h1></div>
    <div class="band band--title"><p class="owner-title">TRANSFORMATIONAL LIFE COACH</p></div>
    <div class="band band--web"><p class="owner-web">www.lorettavanmeer.example</p></div>
  </section>

  <section class="card card--back">
    <div class="scene" role="img" aria-label="Blurred black and white photo of a road and hills at dusk"></div>
    <div class="icon-strip"></div>

    <svg class="strip-icon" style="top:28px" viewBox="0 0 48 48" aria-hidden="true">
      <circle cx="24" cy="16" r="10" fill="var(--strip-icon)"/>
      <path d="M6 44 C6 32 14 28 24 28 C34 28 42 32 42 44 Z" fill="var(--strip-icon)"/>
    </svg>
    <svg class="strip-icon" style="top:134px" viewBox="0 0 48 48" aria-hidden="true">
      <rect x="4" y="10" width="40" height="28" fill="var(--strip-icon)"/>
      <path d="M4 10 L24 28 L44 10 M4 38 L18 23 M44 38 L30 23" fill="none" stroke="var(--strip)" stroke-width="2"/>
    </svg>
    <svg class="strip-icon" style="top:236px" viewBox="0 0 48 48" aria-hidden="true">
      <ellipse cx="24" cy="21" rx="20" ry="14" fill="var(--strip-icon)"/>
      <path d="M12 31 L8 44 L22 34 Z" fill="var(--strip-icon)"/>
    </svg>
    <svg class="strip-icon" style="top:344px" viewBox="0 0 48 48" aria-hidden="true">
      <path d="M12 38 A9 9 0 0 1 12 20 A12 12 0 0 1 34 16 A11 11 0 0 1 36 38 Z" fill="var(--strip-icon)"/>
    </svg>

    <div class="divider"></div>

    <div class="contact-panel">
      <div class="contact-row">
        <svg class="arrow" viewBox="0 0 9 12" aria-hidden="true"><path d="M0 0 L9 6 L0 12 Z" fill="var(--ink)"/></svg>
        <span class="contact-name">Loretta Vanmeer</span>
      </div>
      <div class="contact-row">
        <svg class="arrow" viewBox="0 0 9 12" aria-hidden="true"><path d="M0 0 L9 6 L0 12 Z" fill="var(--ink)"/></svg>
        <span class="contact-text">555-318-4072</span>
      </div>
      <div class="contact-row">
        <svg class="arrow" viewBox="0 0 9 12" aria-hidden="true"><path d="M0 0 L9 6 L0 12 Z" fill="var(--ink)"/></svg>
        <span class="contact-text">loretta@lorettavanmeer.example</span>
      </div>
      <div class="contact-row">
        <svg class="arrow" viewBox="0 0 9 12" aria-hidden="true"><path d="M0 0 L9 6 L0 12 Z" fill="var(--ink)"/></svg>
        <span class="contact-text">www.lorettavanmeer.example</span>
      </div>
    </div>
  </section>

</main>
</body>
</html>
```